Flyer Design

I will be hosting an event at Penrith's amber lantern. Here is a link to their page http://www.theamberlantern.com.au/events-and-workshops/whats-on-penrith/. I have attached the details of my course from their website below. I hope this is of some valuable assistance.

Florist and lover of all things gorgeous, Molly Hartwell from Molly Hartwell Flowers will be running this beautiful and fun workshop. Come along to learn how to make your very own floral crown. All you need to bring are some closed in shoes, an apron and an open mind ready for creativity!

Teens & adults welcome

Date 1: Saturday 11 April 2015
Time 1: 11:00-2:00pm

Date 2: Thursday 23 April 2015
Time 2: 6:00-9:00pm

Cost: $90 per person (includes materials provided – see list below)
Place: The Amber Lantern, Unit 3, 27 Baxter Lane Penrith
RSVP: Molly via email mollyhartwellflowers@fernmail.example or phone 0431 795 206

Materials provided:
• Florist scissors
• Parafilm
• Wire
• Flowers
• light snacks & refreshments

```html
<!DOCTYPE html>
<html lang="en">
<head>
<meta charset="utf-8">
<title>Floral Crowns Workshop Flyer</title>
<link rel="stylesheet" href="https://fonts.googleapis.com/css2?family=Crimson+Text:wght@400;700&family=Dancing+Script:wght@500&display=swap">
<style>
  :root {
    --page: #ffffff;
    --ink: #1c1c1c;
    --pink: #d6337f;
    --teal: #72b8ae;
    --frame: #c9c9c9;
    --photo-top: #d9d6c8;
    --photo-mid: #b9a58f;
    --photo-low: #a9b98f;
  }
  * { margin: 0; padding: 0; box-sizing: border-box; }
  html, body {
    width: 1200px; height: 1000px; overflow: hidden;
    background: var(--page);
  }
  body { position: relative; font-family: "Crimson Text", serif; color: var(--ink); }

  .flyer {
    position: absolute; left: 187px; top: 208px;
    width: 827px; height: 583px;
    background: var(--page);
    border: 1px solid var(--frame);
    box-shadow: 3px 3px 5px rgba(0,0,0,0.35);
  }
  .flyer__content { position: absolute; left: 40px; top: 0; width: 440px; }

  .brand {
    position: absolute; top: 44px; left: 0;
    display: flex; align-items: center; gap: 10px;
  }
  .brand__mark { width: 22px; height: 22px; background: var(--teal); }
  .brand__name {
    font-size: 20px; line-height: 20px; width: 90px;
    font-weight: 400; color: var(--ink);
  }

  .title {
    position: absolute; top: 112px; left: 0; white-space: nowrap;
    font-size: 41px; font-weight: 400; line-height: 48px;
  }
  .presenter {
    position: absolute; top: 160px; left: 0; white-space: nowrap;
    font-family: "Dancing Script", cursive; font-size: 20px; font-weight: 500;
    color: var(--teal);
  }
  .presenter__name { color: var(--pink); }
  .divider {
    position: absolute; top: 198px; left: 0; width: 436px;
    border-top: 3px dotted var(--ink);
  }
  .schedule {
    position: absolute; top: 216px; left: 0;
    font-size: 15.5px; line-height: 22px; text-transform: uppercase;
    white-space: nowrap;
  }
  .body-copy {
    position: absolute; top: 286px; left: 0; width: 440px;
    font-size: 15.5px; line-height: 20px;
  }
  .body-copy p { margin-bottom: 12px; }
  .body-copy .audience { font-weight: 700; margin-bottom: 14px; }
  .details { display: grid; grid-template-columns: 55px 1fr; line-height: 20px; }
  .details dt { font-weight: 700; }
  .link { color: var(--pink); }

  .flyer__photo {
    position: absolute; right: 0; top: 0; width: 276px; height: 583px;
    background: linear-gradient(180deg, var(--photo-top) 0%, var(--photo-mid) 45%, var(--photo-low) 100%);
  }
</style>
</head>
<body>
  <article class="flyer">
    <div class="flyer__content">
      <div class="brand">
        <span class="brand__mark"></span>
        <span class="brand__name">the amber lantern</span>
      </div>

      <h1 class="title">Floral Crowns Workshop</h1>
      <p class="presenter">Presented by <span class="presenter__name">Molly Hartwell Flowers</span></p>
      <div class="divider"></div>

      <div class="schedule">
        <p>Sat, 11 Apr 2015, 11am-2pm • Thu, 23 April 2015, 6-9pm</p>
        <p>The Amber Lantern, Unit 3, 27 Baxter Lane Penrith</p>
      </div>

      <div class="body-copy">
        <p>Florist and lover of all things gorgeous, Molly Hartwell from Molly Hartwell Flowers will be running this beautiful and fun workshop. Come along to learn how to make your very own floral crown. All you need to bring are some closed in shoes, an apron and an open mind ready for creativity!</p>
        <p>Florist scissors, parafilm, wire, flowers materials are provided together with a light snacks &amp; refreshments.</p>
        <p class="audience">Teens &amp; Adults Welcome</p>
        <dl class="details">
          <dt>FEE:</dt><dd>$90 per person (include materials)</dd>
          <dt>RSVP:</dt><dd>Molly via email <span class="link">mollyhartwellflowers@fernmail.example</span> or phone <span class="link">0431 795 206</span></dd>
        </dl>
      </div>
    </div>

    <div class="flyer__photo" role="img" aria-label="Portrait of the florist smiling, wearing a flower in her hair and a floral print top"></div>
  </article>
</body>
</html>
```